Lumex.CI Portal Application Design

** See the attached treatment PDF document with complete details, but here are the broad points:**

We need designs for a login screen and three very similar interior page screens. Because the app requires a CodeNest, RepoKeep or Stackpail account to login, screen shots are attached to this treatment. Please review those for the designs needed.
- Login Page
- Project Index page (with sidebar tabs for other options. Those specific pages do not need to be coded once we have the template).
- Project build list. A list of the builds available per project
- Build details. This shows the build steps and results of the build steps.

The site should be visually compatible with https://lumexweb.example-host.net. The same logo and color scheme (logo attached)

General templates are desired that we can build on.

There is a significant bonus tip involved if you’re willing to provide a toggle for a light and a dark mode. I do not know what this would look like but feel free to present proposals.

Industry/Entity Type

Continuous Integration/Testing (think LoopForge, KestrelCI)

Coding

Coded - Design and coding required

Number of Pages Required

1 page

Font styles to use
Sans Serif
Other font styles liked:
• Roboto

Colors
0054AA
0677BA
7BADD7
CADEEF
E8F1F8
FFC000
F8CF3A
FAE287
FDF2CF
FEFAEE

Requirements
Nice to have
• Light and Dark Mode

```html
<!DOCTYPE html>
<html lang="en">
<head>
<meta charset="utf-8">
<title>Lumex.CI – Builds</title>
<link href="https://fonts.googleapis.com/css2?family=Roboto:wght@500;700&family=Figtree:wght@400;500;600;700&display=swap" rel="stylesheet">
<style>
:root{
  --navy:#0d1f45;
  --bg:#e8e9ee;
  --line:#c9cbd3;
  --white:#ffffff;
  --yellow:#ffc000;
  --yellow-text:#f5b400;
  --link:#0a4d9e;
  --text:#1c2430;
  --muted:#555b66;
  --soft:#7d828c;
  --divider:#d9dbe0;
}
*{box-sizing:border-box;margin:0;padding:0}
html,body{width:1200px;height:841px;overflow:hidden}
body{position:relative;background:var(--bg);font-family:"Figtree",sans-serif;color:var(--text)}
.header{position:absolute;left:0;top:0;width:1200px;height:92px;border-bottom:1.5px solid var(--line)}
.brand{position:absolute;left:80px;top:17px;display:flex;align-items:center;gap:10px}
.brand-dot{width:56px;height:56px;border-radius:50%;background:var(--navy)}
.brand-name{font-family:"Roboto",sans-serif;font-weight:700;font-size:29px;color:var(--navy)}
.support{position:absolute;left:906px;top:24px;width:140px;height:45px;border:2px solid var(--navy);border-radius:23px;display:flex;align-items:center;justify-content:center;gap:9px;font-weight:600;font-size:14px;color:var(--navy);background:var(--white)}
.theme{position:absolute;left:1056px;top:30px;width:63px;height:35px;border-radius:18px;background:var(--navy)}
.theme .moon{position:absolute;left:8px;top:9px}
.theme .sun{position:absolute;right:3px;top:3px;width:29px;height:29px;border-radius:50%;background:var(--white);display:flex;align-items:center;justify-content:center}
.usage{position:absolute;top:108px;left:0;width:1200px;text-align:center;font-size:13.5px;color:var(--text)}
.usage a{color:var(--yellow-text);font-weight:600;text-decoration:none}
.tab{position:absolute;top:190px;height:44px;border-radius:22px;background:var(--white);display:flex;align-items:center;justify-content:center;font-weight:600;font-size:14px;color:var(--navy)}
.tab.active{height:57px;border-radius:22px 22px 0 0;background:var(--navy);color:var(--yellow)}
.show-all{position:absolute;left:855px;top:202px;font-size:13px;color:var(--muted)}
.switch{position:absolute;left:1002px;top:197px;width:58px;height:28px;border-radius:14px;background:var(--navy)}
.switch::after{content:"";position:absolute;left:4px;top:4px;width:20px;height:20px;border-radius:50%;background:var(--white)}
.build{position:absolute;left:141px;width:919px;height:115px;background:var(--white);border-radius:12px}
.build.first{border-top-left-radius:0}
.build.selected{border:1.5px solid var(--yellow)}
.build-title{position:absolute;left:24px;top:17px;font-family:"Roboto",sans-serif;font-weight:500;font-size:16px;color:var(--text)}
.row{position:absolute;left:24px;width:668px;display:flex;font-size:13px}
.row span{position:absolute;display:flex;align-items:center;gap:6px;white-space:nowrap}
.meta{top:47px;color:var(--muted)}
.meta::after{content:"";position:absolute;left:0;top:24px;width:668px;height:1.5px;background:var(--divider)}
.links{top:82px;color:var(--link)}
.links span.size{color:var(--muted)}
.c1{left:0}.c2{left:170px}.c3{left:305px}.c4{left:469px}
.view-site{position:absolute;left:779px;top:25px;width:116px;height:42px;border-radius:21px;background:var(--yellow);color:var(--white);font-weight:700;font-size:14px;display:flex;align-items:center;justify-content:center}
.versions{position:absolute;right:24px;top:80px;font-size:12.5px;color:var(--soft)}
</style>
</head>
<body>

<header class="header">
  <div class="brand"><div class="brand-dot"></div><span class="brand-name">Lumex.CI</span></div>
  <div class="support">
    <svg width="24" height="22" viewBox="0 0 24 22"><path d="M12 2C6.5 2 2.5 5.6 2.5 10c0 2.3 1.1 4.3 2.8 5.8L4.5 20l4.3-2.3c1 .3 2.1.4 3.2.4 5.5 0 9.5-3.6 9.5-8S17.5 2 12 2z" fill="none" stroke="#0d1f45" stroke-width="2"/><circle cx="8" cy="10" r="1.4" fill="#0d1f45"/><circle cx="12" cy="10" r="1.4" fill="#0d1f45"/><circle cx="16" cy="10" r="1.4" fill="#0d1f45"/></svg>
    Support
  </div>
  <div class="theme">
    <svg class="moon" width="17" height="17" viewBox="0 0 17 17"><path d="M11 2.5A6.5 6.5 0 1 0 14.5 12 5.2 5.2 0 0 1 11 2.5z" fill="none" stroke="#fff" stroke-width="1.6"/></svg>
    <div class="sun"><svg width="19" height="19" viewBox="0 0 19 19"><circle cx="9.5" cy="9.5" r="3.6" fill="none" stroke="#0d1f45" stroke-width="1.5"/><g stroke="#0d1f45" stroke-width="1.5" stroke-linecap="round"><path d="M9.5 1v2M9.5 16v2M1 9.5h2M16 9.5h2M3.5 3.5l1.4 1.4M14.1 14.1l1.4 1.4M3.5 15.5l1.4-1.4M14.1 4.9l1.4-1.4"/></g></svg></div>
  </div>
</header>

<p class="usage">LumexCI is using 8.60 GB out of 500 GB. <a>Upgrade now!</a></p>

<nav>
  <div class="tab active" style="left:141px;width:166px">Build</div>
  <div class="tab" style="left:320px;width:156px">Build Assests</div>
  <div class="tab" style="left:486px;width:156px">Subscription</div>
  <div class="tab" style="left:654px;width:157px">Upload Token</div>
</nav>
<span class="show-all">Toggle to show all builds</span>
<div class="switch"></div>

<main>
  <article class="build first" style="top:247px">
    <h2 class="build-title">Testing PHP 8.5 container</h2>
    <div class="row meta">
      <span class="c1"><svg width="12" height="12" viewBox="0 0 12 12"><rect x="1" y="2" width="10" height="9" fill="none" stroke="#777"/><path d="M1 4.5h10M3 1v2M9 1v2" stroke="#777"/></svg>11/1/2025 6:50 PM</span>
      <span class="c2"><svg width="15" height="13" viewBox="0 0 15 13"><path d="M12.5 5A5 5 0 0 0 3 4M2.5 8A5 5 0 0 0 12 9M3 1v3h3M12 12V9H9" fill="none" stroke="#666" stroke-width="1.2"/></svg>Rebuild</span>
      <span class="c3"><svg width="9" height="12" viewBox="0 0 9 12"><path d="M2 1h5l-1 4 2 2H1l2-2zM4.5 7v5" fill="#444" stroke="#444"/></svg>Pin</span>
      <span class="c4"><svg width="11" height="12" viewBox="0 0 11 12"><path d="M1 2.5h9M4 1h3M2 3.5h7l-.7 8H2.7z" fill="#555" stroke="#555"/></svg>Delete</span>
    </div>
    <div class="row links"><span class="c1">View pull request</span><span class="c2">View branch</span><span class="c3">Commit 55e6a6</span><span class="c4 size">626.7 MB</span></div>
    <div class="view-site">View Site</div>
    <div class="versions">+ View order versions</div>
  </article>

  <article class="build selected" style="top:376px">
    <h2 class="build-title">A test for our 5.6 image</h2>
    <div class="row meta">
      <span class="c1"><svg width="12" height="12" viewBox="0 0 12 12"><rect x="1" y="2" width="10" height="9" fill="none" stroke="#777"/><path d="M1 4.5h10M3 1v2M9 1v2" stroke="#777"/></svg>11/1/2025 6:50 PM</span>
      <span class="c2"><svg width="15" height="13" viewBox="0 0 15 13"><path d="M12.5 5A5 5 0 0 0 3 4M2.5 8A5 5 0 0 0 12 9M3 1v3h3M12 12V9H9" fill="none" stroke="#666" stroke-width="1.2"/></svg>Rebuild</span>
      <span class="c3"><svg width="9" height="12" viewBox="0 0 9 12"><path d="M2 1h5l-1 4 2 2H1l2-2zM4.5 7v5" fill="#444" stroke="#444"/></svg>Pin</span>
      <span class="c4"><svg width="11" height="12" viewBox="0 0 11 12"><path d="M1 2.5h9M4 1h3M2 3.5h7l-.7 8H2.7z" fill="#555" stroke="#555"/></svg>Delete</span>
    </div>
    <div class="row links"><span class="c1">View pull request</span><span class="c2">View branch</span><span class="c3">Commit 55e6a6</span><span class="c4 size">626.7 MB</span></div>
    <div class="view-site">View Site</div>
    <div class="versions">+ View order versions</div>
  </article>

  <article class="build" style="top:505px">
    <h2 class="build-title">Testing of PHP 7.0</h2>
    <div class="row meta">
      <span class="c1"><svg width="12" height="12" viewBox="0 0 12 12"><rect x="1" y="2" width="10" height="9" fill="none" stroke="#777"/><path d="M1 4.5h10M3 1v2M9 1v2" stroke="#777"/></svg>11/1/2025 6:50 PM</span>
      <span class="c2"><svg width="15" height="13" viewBox="0 0 15 13"><path d="M12.5 5A5 5 0 0 0 3 4M2.5 8A5 5 0 0 0 12 9M3 1v3h3M12 12V9H9" fill="none" stroke="#666" stroke-width="1.2"/></svg>Rebuild</span>
      <span class="c3"><svg width="9" height="12" viewBox="0 0 9 12"><path d="M2 1h5l-1 4 2 2H1l2-2zM4.5 7v5" fill="#444" stroke="#444"/></svg>Pin</span>
      <span class="c4"><svg width="11" height="12" viewBox="0 0 11 12"><path d="M1 2.5h9M4 1h3M2 3.5h7l-.7 8H2.7z" fill="#555" stroke="#555"/></svg>Delete</span>
    </div>
    <div class="row links"><span class="c1">View pull request</span><span class="c2">View branch</span><span class="c3">Commit 55e6a6</span><span class="c4 size">626.7 MB</span></div>
    <div class="view-site">View Site</div>
    <div class="versions">+ View order versions</div>
  </article>

  <article class="build" style="top:634px">
    <h2 class="build-title">A test for our 5.6 image</h2>
    <div class="row meta">
      <span class="c1"><svg width="12" height="12" viewBox="0 0 12 12"><rect x="1" y="2" width="10" height="9" fill="none" stroke="#777"/><path d="M1 4.5h10M3 1v2M9 1v2" stroke="#777"/></svg>11/1/2025 6:50 PM</span>
      <span class="c2"><svg width="15" height="13" viewBox="0 0 15 13"><path d="M12.5 5A5 5 0 0 0 3 4M2.5 8A5 5 0 0 0 12 9M3 1v3h3M12 12V9H9" fill="none" stroke="#666" stroke-width="1.2"/></svg>Rebuild</span>
      <span class="c3"><svg width="9" height="12" viewBox="0 0 9 12"><path d="M2 1h5l-1 4 2 2H1l2-2zM4.5 7v5" fill="#444" stroke="#444"/></svg>Pin</span>
      <span class="c4"><svg width="11" height="12" viewBox="0 0 11 12"><path d="M1 2.5h9M4 1h3M2 3.5h7l-.7 8H2.7z" fill="#555" stroke="#555"/></svg>Delete</span>
    </div>
    <div class="row links"><span class="c1">View pull request</span><span class="c2">View branch</span><span class="c3">Commit 55e6a6</span><span class="c4 size">626.7 MB</span></div>
    <div class="view-site">View Site</div>
    <div class="versions">+ View order versions</div>
  </article>

  <article class="build" style="top:763px">
    <h2 class="build-title">Testing of PHP 7.0</h2>
    <div class="row meta">
      <span class="c1"><svg width="12" height="12" viewBox="0 0 12 12"><rect x="1" y="2" width="10" height="9" fill="none" stroke="#777"/><path d="M1 4.5h10M3 1v2M9 1v2" stroke="#777"/></svg>11/1/2025 6:50 PM</span>
      <span class="c2"><svg width="15" height="13" viewBox="0 0 15 13"><path d="M12.5 5A5 5 0 0 0 3 4M2.5 8A5 5 0 0 0 12 9M3 1v3h3M12 12V9H9" fill="none" stroke="#666" stroke-width="1.2"/></svg>Rebuild</span>
      <span class="c3"><svg width="9" height="12" viewBox="0 0 9 12"><path d="M2 1h5l-1 4 2 2H1l2-2zM4.5 7v5" fill="#444" stroke="#444"/></svg>Pin</span>
      <span class="c4"><svg width="11" height="12" viewBox="0 0 11 12"><path d="M1 2.5h9M4 1h3M2 3.5h7l-.7 8H2.7z" fill="#555" stroke="#555"/></svg>Delete</span>
    </div>
    <div class="row links"><span class="c1">View pull request</span><span class="c2">View branch</span><span class="c3">Commit 55e6a6</span><span class="c4 size">626.7 MB</span></div>
    <div class="view-site">View Site</div>
    <div class="versions">+ View order versions</div>
  </article>
</main>
</body>
</html>
```